依頼詳細
<現状サイトの課題>
①一目で、何をしている会社なのかが分からない。
⇒商品画像・作業画像などを入れ、分かりやすく目を引き付けるようにする。

②項目が小さく、引き付けにくいデザイン。
⇒アイコンを大きくして、デザイン性を持たせる。

③自社の強みを視覚化できていない。
⇒図や写真を追加し、視覚的に伝わるようにする。

④自社の新着情報がないので社内の動きが把握できない。
⇒新着ニュースを追加し社内の動きが把握できるようにする。

⑤企業規模が小さく感じてしまう。
⇒洗練されたデザイン、コンテンツの充実、グローバルサイトの作成により企業規模をワンランク大きく見えるように表現する。
----------------------------------
<現在のサイト>
明確なサイトの情報共有はできませんが、TOPページの情報を一部伏せて共有します。添付の”TOPページ”をご参照ください。

<サイトリニューアルの方針>
①強みを明確にする為、全体的に画像化し打ち出したい。TOPページは動画を掲載し、よりリアルにユーザー様にイメージが伝わるデザインにする。

②企業規模をワンランク大きく見えるように表現し、グローバル化についてもアピールすることで、事業規模の大きい信頼出来る会社であることが分かるようにし、新規顧客の獲得および定着するようにサイトリニューアルを行う。

③必須機能
・TOPページへ動画を埋め込む。
・スマホ対応(レスポンシブウェブデザイン)にする。
・ウェブ見積り機能を設け、いつでも見積りが確認できるようにする。(TOPページにバナーを設けるなどデザインする)

<イメージ参考サイト>
①メインカラーをブルーとし、TOPページを開くとすぐに大きな画像イメージが見えます。
https://www.e-hariwa.co.jp/

②トップページに表示される、動画イメージです。
https://www.dovel.co.jp/

③コンテンツの配置や施工事例が見やすいです。
http://www.tasemi-kk.com/

④TOPページに施工写真や文字が挿入されており分かりやすい。また企業イメージがよく考えられており、ブランディングされています。
http://www.fujiyaga.co.jp/

<カラーテーマ>
①青系(堅実・信頼・クール)または水色系(さわやか・清潔感)

②青4割、白6割の配色のイメージでお願いします。制作の際は、カラーチャート(カラーを選んだ理由)もご提示いただけると幸いです。

<重視する点/検討基準>
①サイトコンセプトにあったデザイン(ご提案の際は、制作頂いたデザインコンセプト及びデザイン説明コメントの記載をお願い致します)

②納期厳守

<具体的な制作数>
TOPページ:1ページ(PC版のデザイン制作をお願いします)

<選考の進め方>
ご提案頂いたデザイン内容・コンセプトなどをもとに、プロジェクトメンバーで選考、決定致します。
※今回は、トップページデザインのみの見積りとなります。
今後、コーディングを依頼する可能性もございます。その場合は改めてクリエタスを通じてご依頼させて頂きます。パララックスデザインでのコーディングも条件として入れてまいります。
1ページ
青系、水色系
• イラストレーター形式 (.ai)
• フォトショップ形式 (.psd)
追記です。
サイトコンセプトの資料も添付いたします。
宜しくお願いいたします。

クライアント様と協議させていただき、コンセプトに合った総合的なデザインを評価させて頂きました。
その中で、クライアント様からの評価が多かった「Pixfern様」を当選とさせていただきました。ありがとうございました。

ランサーの皆さん、このように沢山の素敵なデザインをご提案頂き本当にありがとうございました。
コンセプトを基に、クライアント様とも大いに悩んで決定させて頂きました。
また、選定が期限間近になってしまいましたこと、申し訳ございませんでした。

機会があれば、今後ともどうぞ宜しくお願い致します。

```html
<!DOCTYPE html>
<html lang="ja">
<head>
<meta charset="utf-8">
<title>会社トップページ</title>
<link href="https://fonts.googleapis.com/css2?family=Noto+Sans+JP:wght@400;500;700&family=Oswald:wght@500&display=swap" rel="stylesheet">
<style>
:root{
  --blue:#1d6fae;
  --blue-dark:#12507f;
  --sky:#e7f1f8;
  --red:#d2262b;
  --ink:#333;
  --muted:#777;
  --line:#dde3e8;
  --dark:#2a2420;
  --paper:#fff;
  --foot:#eef2f5;
}
*{box-sizing:border-box;margin:0;padding:0}
html,body{width:1200px;height:3340px;overflow:hidden}
body{font-family:"Noto Sans JP",sans-serif;color:var(--ink);background:var(--paper);position:relative}
.abs{position:absolute}
.site-header{position:absolute;top:0;left:0;width:1200px;height:92px}
.logo{position:absolute;left:80px;top:14px;font-size:26px;font-weight:700;color:var(--blue)}
.head-btn{position:absolute;top:8px;height:32px;width:110px;color:#fff;font-size:12px;display:flex;align-items:center;justify-content:center;gap:6px}
.head-btn.est{left:900px;background:var(--red)}
.head-btn.contact{left:1016px;background:var(--blue)}
.global-nav{position:absolute;top:62px;left:150px;display:flex;gap:30px;font-size:13px;color:var(--ink)}
.global-nav span:first-child{color:var(--blue);font-weight:700}
.hero{position:absolute;top:92px;left:0;width:1200px;height:508px;background:radial-gradient(ellipse at 50% 40%,#f4f6f8 0%,#b9c0c6 45%,#6e767d 100%)}
.hero-copy{position:absolute;top:300px;left:0;width:1200px;text-align:center;color:#fff;font-size:28px;font-weight:500;letter-spacing:2px;text-shadow:0 1px 4px rgba(0,0,0,.7)}
.strength{position:absolute;top:600px;left:0;width:1200px;height:660px;background:linear-gradient(#fff,#f6f8fa)}
.sec-heading{position:absolute;top:48px;left:0;width:1200px;text-align:center;font-size:24px;font-weight:700}
.card{position:absolute;top:100px;width:256px;height:270px;background:var(--sky)}
.card .photo{height:150px;background:linear-gradient(135deg,#c9d2d9,#8e9aa4)}
.card .num{position:absolute;top:124px;left:103px;width:50px;height:50px;border-radius:50%;background:var(--blue);color:#fff;border:3px solid #fff;font-size:22px;display:flex;align-items:center;justify-content:center;font-weight:700}
.card p{position:absolute;top:186px;left:0;width:256px;text-align:center;font-size:15px;font-weight:500;line-height:1.7}
.intro{position:absolute;top:396px;left:185px;width:830px;font-size:13px;line-height:1.9}
.btn{position:absolute;height:38px;width:150px;background:var(--blue);color:#fff;font-size:13px;display:flex;align-items:center;justify-content:center;gap:8px}
.works{position:absolute;top:1260px;left:0;width:1200px;height:880px}
.title-en{position:absolute;left:0;width:1200px;text-align:center;font-family:"Oswald",sans-serif;font-size:34px;letter-spacing:2px}
.title-ja{position:absolute;left:0;width:1200px;text-align:center;font-size:12px;color:var(--muted)}
.work{position:absolute;width:240px}
.work .photo{height:250px;background:linear-gradient(160deg,#e3e6e9,#9aa2a8 60%,#5f676d)}
.work p{text-align:center;font-size:13px;margin-top:14px}
.info{position:absolute;top:2140px;left:0;width:1200px;height:660px;background:linear-gradient(160deg,#4a3a2e,#1f1a17 50%,#3c4148)}
.panel{position:absolute;top:140px;width:420px;height:330px;background:#fff}
.panel h3{height:40px;background:var(--blue);color:#fff;font-size:15px;font-weight:500;display:flex;align-items:center;justify-content:center}
.news{list-style:none;padding:18px 26px}
.news li{font-size:12px;padding:9px 0;border-bottom:1px dotted var(--line);display:flex;gap:16px}
.news li b{color:var(--blue);font-weight:500}
.blog{display:flex;align-items:center;gap:14px;padding:12px 26px;border-bottom:1px dotted var(--line);font-size:12px}
.blog .thumb{width:70px;height:56px;background:linear-gradient(135deg,#cfd6dc,#8a949c);flex:none}
.recruit{position:absolute;top:2800px;left:0;width:1200px;height:240px;background:#f7f9fb}
.recruit .side{position:absolute;top:0;height:240px;width:340px}
.footer{position:absolute;top:3040px;left:0;width:1200px;height:300px;background:var(--foot)}
.banner{position:absolute;top:110px;left:160px;width:480px;height:84px;background:var(--blue);color:#fff;padding:14px 30px}
.banner strong{font-size:16px;font-weight:500;display:block}
.banner small{font-size:12px}
.tel{position:absolute;top:106px;left:700px;font-size:34px;font-weight:700;display:flex;align-items:center;gap:10px}
.foot-nav{position:absolute;top:226px;left:0;width:1200px;display:flex;justify-content:center;gap:24px;font-size:12px}
.copyright{position:absolute;top:266px;left:0;width:1200px;height:34px;background:var(--blue-dark);color:#dde8f1;font-size:11px;display:flex;align-items:center;justify-content:center}
</style>
</head>
<body>
<header class="site-header">
  <div class="logo">会社ロゴ</div>
  <div class="head-btn est">Web見積依頼</div>
  <div class="head-btn contact">お問い合わせ</div>
  <nav class="global-nav"><span>HOME</span><span>会社概要</span><span>事業紹介</span><span>採用情報</span><span>スタッフ紹介</span><span>社内報</span><span>ブログ</span></nav>
</header>

<section class="hero" role="img" aria-label="螺旋階段を見上げた鉄骨建築の写真">
  <p class="hero-copy">高品質・短納期の鉄製品の製造を提供いたします</p>
</section>

<section class="strength">
  <h2 class="sec-heading">鉄製品の製造・工事の『高品質・短納期』を実現</h2>
  <div class="card" style="left:185px"><div class="photo" role="img" aria-label="製造現場の写真"></div><div class="num">1</div><p>「高品質・短納期」を<br>ご実現いただけるサービス</p></div>
  <div class="card" style="left:472px"><div class="photo" role="img" aria-label="打ち合わせの写真"></div><div class="num">2</div><p>何でもご相談いただける<br>柔軟な体制</p></div>
  <div class="card" style="left:759px"><div class="photo" role="img" aria-label="スタッフの写真"></div><div class="num">3</div><p>常にお客様目線で取り組み<br>成長し続ける姿勢</p></div>
  <p class="intro">当社は、地域を中心に鉄製品の製造・施工を行っております。階段や手すりなどの鉄部製品を、設計から工事まで一貫して承ります。お客様に喜んでいただけるよう、常に品質の向上に努め、「高品質・短納期」を実現いたしました。<br>鉄製品の製造・工事のことなら、当社にお気軽にご相談ください。</p>
  <div class="btn" style="top:526px;left:440px">会社概要へ ›</div>
  <div class="btn" style="top:526px;left:610px">事業案内へ ›</div>
</section>

<section class="works">
  <h2 class="title-en" style="top:40px;color:var(--blue)">WORKS</h2>
  <p class="title-ja" style="top:88px">施工事例</p>
  <div class="work" style="left:185px;top:125px"><div class="photo" role="img" aria-label="螺旋階段の施工写真"></div><p>螺旋階段</p></div>
  <div class="work" style="left:480px;top:125px"><div class="photo" role="img" aria-label="非常階段の施工写真"></div><p>非常階段</p></div>
  <div class="work" style="left:775px;top:125px"><div class="photo" role="img" aria-label="螺旋階段の施工写真"></div><p>螺旋階段</p></div>
  <div class="work" style="left:185px;top:455px"><div class="photo" role="img" aria-label="非常階段の施工写真"></div><p>非常階段</p></div>
  <div class="work" style="left:480px;top:455px"><div class="photo" role="img" aria-label="螺旋階段の施工写真"></div><p>螺旋階段</p></div>
  <div class="work" style="left:775px;top:455px"><div class="photo" role="img" aria-label="非常階段の施工写真"></div><p>非常階段</p></div>
  <div class="btn" style="top:780px;left:515px;width:170px">施工事例一覧へ ›</div>
</section>

<section class="info" role="img" aria-label="ガラス張りの建物内部の写真を暗く敷いた背景">
  <h2 class="title-en" style="top:60px;color:#fff">INFORMATION</h2>
  <p class="title-ja" style="top:106px;color:#ccc">新着情報</p>
  <div class="panel" style="left:170px">
    <h3>新着情報</h3>
    <ul class="news">
      <li><b>20XX.00.00</b>ホームページをリニューアルしました</li>
      <li><b>20XX.00.00</b>夏季休業のお知らせを掲載しました</li>
      <li><b>20XX.00.00</b>新しい施工事例を追加しました</li>
      <li><b>20XX.00.00</b>採用情報を更新しました</li>
      <li><b>20XX.00.00</b>社内報の最新号を公開しました</li>
    </ul>
    <div class="btn" style="top:272px;left:135px">一覧へ ›</div>
  </div>
  <div class="panel" style="left:610px">
    <h3>ブログ</h3>
    <div class="blog"><div class="thumb" role="img" aria-label="ブログ記事の写真"></div><div><b style="color:var(--blue);font-weight:500">20XX.00.00</b><br>現場の様子をご紹介します</div></div>
    <div class="blog"><div class="thumb" role="img" aria-label="ブログ記事の写真"></div><div><b style="color:var(--blue);font-weight:500">20XX.00.00</b><br>新しい仲間が加わりました</div></div>
    <div class="btn" style="top:272px;left:135px">一覧へ ›</div>
  </div>
</section>

<section class="recruit">
  <div class="side" style="left:0;background:linear-gradient(90deg,#dfe4e8,#f7f9fb)" role="img" aria-label="作業着と図面の写真"></div>
  <div class="side" style="left:860px;background:linear-gradient(270deg,#9aa1a8,#f7f9fb)" role="img" aria-label="スーツの写真"></div>
  <h2 class="title-en" style="top:44px;color:var(--blue)">RECRUIT</h2>
  <p class="title-ja" style="top:92px">採用情報</p>
  <div class="btn" style="top:130px;left:525px">採用情報へ ›</div>
</section>

<footer class="footer">
  <div class="logo" style="left:0;width:1200px;text-align:center;top:36px;font-size:24px">会社ロゴ</div>
  <div class="banner"><strong>お見積もり・お問い合わせはこちらから ›</strong><small>お気軽にご相談・お問い合わせください</small></div>
  <div class="tel">
    <svg width="30" height="30" viewBox="0 0 24 24"><circle cx="12" cy="12" r="12" fill="var(--blue)"/><path d="M8 6l2 0 1 3-1.5 1a7 7 0 0 0 4 4l1-1.5 3 1v2c0 1-1 1.5-2 1.5A10 10 0 0 1 6.5 8C6.5 7 7 6 8 6z" fill="#fff"/></svg>000-000-0000
  </div>
  <p class="abs" style="top:150px;left:740px;font-size:11px;color:var(--muted)">受付時間：平日 00:00〜00:00</p>
  <div class="head-btn est" style="top:172px;left:740px">Web見積依頼</div>
  <div class="head-btn contact" style="top:172px;left:856px">お問い合わせ</div>
  <nav class="foot-nav"><span>HOME</span><span>会社概要</span><span>事業紹介</span><span>採用情報</span><span>スタッフ紹介</span><span>社内報</span><span>ブログ</span><span>Web見積依頼</span><span>お問い合わせ</span></nav>
  <div class="copyright">Copyright © 20XX Company All Rights Reserved.</div>
</footer>
</body>
</html>
```